Hochwertiges Etiketten-Design für edle Destillate
Zielgruppe
Wir sind ein Familiengeführter Brennereibetrieb wo wir edle Destillate (Obstbrände und Liköre) herstellen.
Aufgabenstellung
Wir suchen ein hochwertiges Etikett welches eine sofortige Wiedererkennung hat. Unser jetziges Etikett soll als Vorlage gelten, jedoch einiges aufgewertet werden. Unser Logo und und die Farbe Rot soll auf jeden Fall darin vorkommen.
Dies sind unsere verwendeten Flaschen
https://www.vandoro.com/kelm-flasche-500ml-weissglas-mdg.-gpi-28-karton-50stk.html?cPath=5_6
https://www.vandoro.com/kelm-flasche-200ml-weissglas-mdg.-gpi-28-karton-45stk.html?cPath=5_6
https://www.vandoro.com/urma-500-ml-weissglas-mdg.-gpi-28-karton-46stk.html?cPath=5_6
https://www.vandoro.com/urma-200ml-weissglas-mdg.-gpi-28-karton-90stk.html?cPath=5_6
das Design soll skalierbar und auf andere Größen anwendbar sein
Folgende Angaben müssen auf dem Etikett sein (austauschbar):
-Sorte: z.B. Williams
-Produkt: zB. Birnenbrand
-Losnummer: z.B. K3F57382
-Inhalt: z.B. 500ml
-Alkoholgehalt: 40% vol
-Adresse

```html
<!DOCTYPE html>
<html lang="de">
<head>
<meta charset="utf-8">
<title>Williams – Etikett</title>
<link rel="stylesheet" href="https://fonts.googleapis.com/css2?family=Short+Stack&family=Tinos&family=Arimo:wght@400;600&display=swap">
<style>
  :root {
    --page: #ffffff;
    --label-black: #000000;
    --label-red: #8e0f2e;
    --label-white: #ffffff;
    --art-glow: #a02240;
    --brand-grey: #505058;
    --ink: #111111;
  }
  html, body {
    margin: 0;
    padding: 0;
    width: 849px;
    height: 1200px;
    overflow: hidden;
    background: var(--page);
  }
  .label {
    position: absolute;
    left: 64px;
    top: 60px;
    width: 720px;
    height: 1080px;
    display: block;
  }
  .label__black { fill: var(--label-black); }
  .label__red { fill: var(--label-red); }
  .label__white { fill: var(--label-white); }
  .label__art-glow { stop-color: var(--art-glow); }
  .label__art-edge { stop-color: var(--label-red); }
  .label__variety {
    font-family: "Short Stack", cursive;
    font-size: 68px;
    fill: var(--label-white);
  }
  .label__brand-mark { fill: var(--brand-grey); }
  .label__brand-name {
    font-family: "Arimo", sans-serif;
    font-weight: 600;
    font-size: 17px;
    fill: var(--brand-grey);
  }
  .label__volume {
    font-family: "Tinos", serif;
    font-size: 20px;
    fill: var(--ink);
  }
  .label__abv {
    font-family: "Arimo", sans-serif;
    font-size: 19px;
    fill: var(--ink);
  }
  .label__lot {
    font-family: "Tinos", serif;
    font-size: 17px;
    letter-spacing: 1px;
    fill: var(--ink);
  }
</style>
</head>
<body>
<svg class="label" viewBox="0 0 502 753" xmlns="http://www.w3.org/2000/svg">
  <defs>
    <radialGradient id="art-glow" cx="0.5" cy="0.5" r="0.5">
      <stop class="label__art-glow" offset="0"/>
      <stop class="label__art-edge" offset="1"/>
    </radialGradient>
  </defs>

  <rect class="label__red" x="0" y="0" width="502" height="753"/>
  <polygon class="label__black" points="0,0 502,0 0,390"/>
  <polygon class="label__white" points="0,390 230,753 0,753"/>

  <text class="label__variety" x="27" y="97">Williams</text>

  <ellipse cx="315" cy="440" rx="175" ry="180" fill="url(#art-glow)"
           role="img" aria-label="Feine weiße Linienzeichnung zweier Birnen"/>

  <circle class="label__brand-mark" cx="64" cy="560" r="20"/>
  <text class="label__brand-name" x="11" y="600">Albrechter</text>

  <text class="label__volume" x="23" y="703">500ml</text>
  <text class="label__abv" x="23" y="730">40% vol</text>

  <text class="label__lot" transform="translate(489 722) rotate(-90)">K3F57382</text>
</svg>
</body>
</html>
```